Online Sofa/Lounge Business needing a Brochure Design

We need a brochure design for a designer online sofa/lounge retailer.
We are a new company based in Sydney and our aim is to make designer lounges accessible to everyone through our lower pricing scheme due to us being an online retailer with low overheads.
Ideally we would like the brochure to be able to be altered by us once the final design is approved so we can edit and add new designs as they are available and change descriptions, pricing etc. and the main brochure design will remain.
The purpose of this brochure is to show clients in face to face meetings, and also marketing purposes such as letterbox drops.
Attached is a basic outline of what we were aiming for originally and are now ready for a finalised design.
I would like to keep the front cover quite similar to how it is now, simple and elegant. I like the whites and don't think adding in other strong colors is what I am looking for.
Target Market(s)
High End
Industry/Entity Type
Marketing
Requirements
Must have
- The layout shall be A5, with the front cover similar to the design I uploaded. The front page must have the web address at the bottom "harbournest.com.au"
- The center two pages shall have smaller pictures containing the sofa's that I have uploaded. Preferably spread out a little so they are not touching or overlapping. I would like to keep the inside similar to the front cover in terms of style. Once i feel the design is right I will be adding some text ie; names of designs and a brief description. The bottom of both pages must have the web address "harbournest.com.au"
- The back cover shall have a large logo and a brief company overview (to be confirmed) and the website address "harbournest.com.au"

```html
<!DOCTYPE html>
<html lang="en">
<head>
<meta charset="utf-8">
<title>Harbour Nest – Brochure Covers</title>
<link rel="stylesheet" href="https://fonts.googleapis.com/css2?family=Lato:wght@300;400&family=Roboto+Condensed:wght@700&family=Open+Sans:wght@400&display=swap">
<style>
  :root {
    --backdrop: #e6e4e1;
    --paper: #ffffff;
    --ink: #1a1a1a;
    --band-1: #555555;
    --band-2: #3b3b3b;
    --band-3: #262626;
    --band-4: #141414;
    --on-dark: #ffffff;
    --on-dark-soft: #d8d8d8;
    --web-bar: #2b2b2b;
  }
  * { box-sizing: border-box; margin: 0; padding: 0; }
  html, body { width: 1200px; height: 900px; overflow: hidden; }
  body { background: var(--backdrop); position: relative; font-family: "Lato", sans-serif; }

  .spread {
    position: absolute; left: 63px; top: 70px;
    width: 1074px; height: 760px;
    display: flex;
    box-shadow: 0 10px 30px rgba(0,0,0,.18);
  }
  .page { position: relative; width: 537px; height: 760px; overflow: hidden; background: var(--paper); }

  /* Back cover */
  .band { position: absolute; left: 0; top: 0; }
  .band--1 { width: 537px; height: 330px; background: var(--band-1); }
  .band--2 { top: 38px; width: 492px; height: 292px; background: var(--band-2); }
  .band--3 { top: 74px; width: 452px; height: 256px; background: var(--band-3); }
  .band--4 { top: 112px; width: 408px; height: 218px; background: var(--band-4); }

  .about { position: absolute; left: 34px; top: 150px; width: 360px; color: var(--on-dark); }
  .about__title { font-family: "Roboto Condensed", sans-serif; font-weight: 700; font-size: 18px; letter-spacing: .5px; margin-bottom: 8px; }
  .about__body { font-family: "Open Sans", sans-serif; font-size: 9.5px; line-height: 1.45; color: var(--on-dark-soft); text-align: justify; }

  .back-photo {
    position: absolute; left: 0; top: 330px; width: 537px; height: 430px;
    background:
      linear-gradient(90deg, #ffffff 0%, rgba(255,255,255,.85) 22%, rgba(255,255,255,0) 48%),
      linear-gradient(180deg, #b9c2c6 0%, #cdd4d6 28%, #e4e7e6 44%, #f2f2ef 58%, #d9dcdb 72%, #eeeeec 86%, #f8f8f7 100%);
  }

  .brand { position: absolute; display: flex; flex-direction: column; align-items: flex-start; }
  .brand__mark { background: var(--ink); }
  .brand__name { font-family: "Lato", sans-serif; font-weight: 300; color: var(--ink); letter-spacing: 2px; white-space: nowrap; }

  .brand--back { left: 30px; top: 548px; }
  .brand--back .brand__mark { width: 120px; height: 112px; }
  .brand--back .brand__name { font-size: 26px; margin-top: 8px; }

  .web-bar {
    position: absolute; right: 0; height: 40px;
    background: var(--web-bar); color: var(--on-dark);
    display: flex; align-items: center; justify-content: center;
    font-family: "Lato", sans-serif; font-weight: 400; font-size: 19px; letter-spacing: 1.5px;
  }
  .web-bar--back { left: 190px; top: 612px; }
  .web-bar--front { left: 250px; top: 690px; }

  /* Front cover */
  .front-photo {
    position: absolute; inset: 0;
    background:
      radial-gradient(ellipse 60% 18% at 38% 92%, rgba(70,70,66,.45) 0%, rgba(70,70,66,0) 100%),
      radial-gradient(ellipse 18% 20% at 22% 66%, rgba(140,128,30,.55) 0%, rgba(140,128,30,0) 100%),
      radial-gradient(ellipse 55% 14% at 72% 58%, rgba(255,253,245,1) 0%, rgba(246,243,234,0) 100%),
      radial-gradient(ellipse 22% 6% at 42% 3%, rgba(205,175,110,.6) 0%, rgba(205,175,110,0) 100%),
      linear-gradient(180deg, #cfcdca 0%, #d9d8d5 30%, #e3e2de 48%, #ecebe6 60%, #f3f3f1 78%, #e4e3e0 100%);
  }
  .front-panel {
    position: absolute; left: 40px; top: 196px; width: 300px; height: 250px;
    background: rgba(255,255,255,.9);
    box-shadow: 0 0 0 22px rgba(255,255,255,.35);
  }
  .brand--front { left: 32px; top: 28px; }
  .brand--front .brand__mark { width: 104px; height: 98px; }
  .brand--front .brand__name { font-size: 24px; margin-top: 8px; }
  .tagline {
    position: absolute; left: 32px; top: 186px;
    font-family: "Lato", sans-serif; font-weight: 400; font-size: 17px; color: var(--ink); letter-spacing: .5px;
    white-space: nowrap;
  }
</style>
</head>
<body>
  <div class="spread">
    <section class="page page--back">
      <div class="band band--1"></div>
      <div class="band band--2"></div>
      <div class="band band--3"></div>
      <div class="band band--4"></div>

      <div class="about">
        <h2 class="about__title">ABOUT US :</h2>
        <p class="about__body">Lorem ipsum dolor sit amet, consectetuer adipiscing elit, sed diam nonummy nibh euismod tincidunt ut laoreet dolore magna aliquam erat volutpat. Ut wisi enim ad minim veniam, quis nostrud exerci tation ullamcorper suscipit lobortis nisl ut aliquip ex ea commodo consequat. Duis autem vel eum iriure dolor in hendrerit in vulputate velit esse molestie consequat, vel illum dolore eu feugiat nulla facilisis at vero eros et accumsan et iusto odio dignissim</p>
      </div>

      <div class="back-photo" role="img" aria-label="Photo of a white sofa with a patterned cushion in a pale living room with framed pictures"></div>

      <div class="brand brand--back">
        <div class="brand__mark"></div>
        <span class="brand__name">HARBOUR NEST</span>
      </div>

      <div class="web-bar web-bar--back">HARBOURNEST.COM.AU</div>
    </section>

    <section class="page page--front">
      <div class="front-photo" role="img" aria-label="Photo of a bright living room with a white sectional sofa, olive throw, rug, crystal chandelier and framed prints"></div>
      <div class="front-panel">
        <div class="brand brand--front">
          <div class="brand__mark"></div>
          <span class="brand__name">HARBOUR NEST</span>
        </div>
        <p class="tagline">LUXURY DESIGNED LIVING</p>
      </div>
      <div class="web-bar web-bar--front">HARBOURNEST.COM.AU</div>
    </section>
  </div>
</body>
</html>
```